Cover design for new academic journal on deconstruction and psychoanalysis

We need a cover for a new academic journal on deconstruction and psychoanalysis. The name of the journal is "The Liminal Remainder: A Journal of Deconstruction and Psychoanalysis" (LR) and it is published by the Calloway Ridge University Press(CRP).

Here is a description of the journal on the CRP website:

http://www.callowayridgepress.example.edu/product/The-Liminal-Remainder,482917.aspx

We are looking for a design that is more abstract and does not have icons or photographs of people, especially not photos of Valmont or Kessler. The design should be contemporary with clean lines and simple fonts. Again, it should be abstract, with no icons or iconography.

The cover should simply have the full name of the journal and then "Volume 1, Issue 1, 2014" on the cover and "Vol. 1, No. 1, 2014" on the spine.

Attached you can see some ideas that we rejected from CRP. It is important that you understand that these designs were rejected and are just being offered as examples of what the cover will look like in general, as a template of sorts.

The cover should have a bold abstract design, with a space for the title and "Volume 1, Issue 1, 2014."

Something bold and contemporary.

Academics, scholars and psychoanalysts.

University

Sans Serif

• Must be abstract, bold, have color, and must be contemporary.
• No icons, no photographs of Valmont, Kessler, or anyone.

```html
<!DOCTYPE html>
<html lang="en">
<head>
<meta charset="utf-8">
<title>The Liminal Remainder — Journal Cover</title>
<link rel="stylesheet" href="https://fonts.googleapis.com/css2?family=Montserrat:wght@300;400;800&display=swap">
<style>
  :root {
    --page: #ffffff;
    --cover: #000000;
    --ink: #ffffff;
    --green: #2fd04a;
    --yellow: #d7c21a;
    --red: #e0203a;
    --magenta: #b0208a;
    --violet: #5a2ad0;
    --teal: #1f9a86;
  }
  html, body {
    margin: 0;
    width: 1200px;
    height: 1000px;
    overflow: hidden;
    background: var(--page);
  }
  .canvas {
    position: relative;
    width: 1200px;
    height: 1000px;
  }
  .cover {
    position: absolute;
    left: 181px;
    top: 90px;
    width: 559px;
    height: 778px;
    background: var(--cover);
    color: var(--ink);
    font-family: "Montserrat", sans-serif;
    overflow: hidden;
  }
  .spine-line {
    position: absolute;
    left: 8px;
    top: 12px;
    writing-mode: vertical-rl;
    font-size: 15px;
    white-space: nowrap;
    font-weight: 300;
    letter-spacing: 0.2px;
  }
  .spine-line .spine-title { font-weight: 800; margin-bottom: 6px; }
  .spine-issue {
    position: absolute;
    left: 8px;
    bottom: 38px;
    writing-mode: vertical-rl;
    font-size: 14px;
    font-weight: 300;
    white-space: nowrap;
    word-spacing: 3px;
  }
  .issue {
    position: absolute;
    right: 50px;
    top: 36px;
    font-size: 14px;
    font-weight: 300;
    white-space: nowrap;
  }
  .artwork {
    position: absolute;
    border-radius: 50%;
    filter: blur(14px);
    opacity: 0.55;
  }
  .artwork--upper {
    left: 110px;
    top: 0;
    width: 270px;
    height: 245px;
    background: linear-gradient(180deg, var(--green) 0%, var(--yellow) 40%, var(--red) 65%, var(--magenta) 82%, var(--violet) 100%);
    border-radius: 40% 40% 50% 50%;
    transform: scaleX(0.9);
  }
  .artwork--lower {
    left: 75px;
    top: 372px;
    width: 340px;
    height: 406px;
    background: linear-gradient(180deg, var(--green) 0%, var(--yellow) 18%, var(--red) 36%, var(--magenta) 55%, var(--violet) 75%, var(--teal) 100%);
    border-radius: 45% 45% 40% 40%;
  }
  .masthead {
    position: absolute;
    left: 77px;
    top: 286px;
  }
  .masthead .title {
    margin: 0;
    font-size: 26.5px;
    font-weight: 800;
    letter-spacing: -0.2px;
    line-height: 1.1;
  }
  .masthead .subtitle {
    margin: 2px 0 0;
    font-size: 18px;
    font-weight: 300;
    letter-spacing: 0.2px;
    white-space: nowrap;
  }
  .publisher {
    position: absolute;
    right: 50px;
    bottom: 46px;
    font-size: 13px;
    font-weight: 400;
    white-space: nowrap;
  }
</style>
</head>
<body>
<div class="canvas">
  <section class="cover">
    <div class="spine-line"><span class="spine-title">The Liminal Remainder</span> A Journal of Deconstruction and Psychoanalysis</div>
    <div class="spine-issue">Vol. 1, No. 1, 2014</div>

    <div class="issue">Volume 1, Issue 1, 2014</div>

    <div class="artwork artwork--upper" role="img" aria-label="Abstract rainbow ribbon of light swirling downward, green to violet"></div>
    <div class="artwork artwork--lower" role="img" aria-label="Abstract rainbow ribbon of light coiling in wide loops, green through red and violet to teal"></div>

    <header class="masthead">
      <h1 class="title">The Liminal Remainder</h1>
      <p class="subtitle">A Journal of Deconstruction and Psychoanalysis</p>
    </header>

    <div class="publisher">Calloway Ridge University Press</div>
  </section>
</div>
</body>
</html>
```